Lindavo Civic Growth Planning New web site

Design a new web site. I have a budget of $1,500.00.
Attached on PowerPoint is a complete site plan. Home page and linked pages.
10 - 12 pages. All copy and photos will be supplied. (300dpi)
I have shown them the concept which they like.
No data bases required. Home page with animations dissolving.
They former web site has been taken down. They have been in business 30 years in New Jersey
Colors teal blues and greens
There will be a new logo)being designed)
The text in home page copy will give you a detailed story what they are all about.
Updates

files have been approved for Lindavo, Inc.   Teodor is the designer

Industry/Entity Type

Community

```html
<!DOCTYPE html>
<html lang="en">
<head>
<meta charset="utf-8">
<title>Lindavo, Inc. — Community Development and Housing Rehabilitation</title>
<link rel="stylesheet" href="https://fonts.googleapis.com/css2?family=Roboto+Condensed:wght@400;500&family=Noto+Sans:wght@400&display=swap">
<style>
  :root {
    --teal: #1e9198;
    --ink: #111111;
    --body-text: #1a1a1a;
    --muted: #8a8a8a;
    --nav-bg: #000000;
    --highlight: #f6ef86;
    --panel-border: #d6d6d6;
    --white: #ffffff;
  }
  * { margin: 0; padding: 0; box-sizing: border-box; }
  html, body { width: 1200px; height: 1200px; overflow: hidden; background: var(--white); }
  body { position: relative; font-family: "Noto Sans", sans-serif; color: var(--body-text); }

  .brand { position: absolute; left: 79px; top: 38px; font-family: "Roboto Condensed", sans-serif; font-weight: 500; font-size: 40px; color: var(--teal); letter-spacing: -0.5px; }
  .brand-divider { position: absolute; left: 311px; top: 50px; width: 1px; height: 26px; background: #b5b5b5; }
  .tagline { position: absolute; left: 331px; top: 57px; font-family: "Roboto Condensed", sans-serif; font-size: 14px; color: var(--muted); }

  .social { position: absolute; top: 52px; left: 921px; display: flex; gap: 13px; }
  .social span { width: 28px; height: 28px; border-radius: 50%; display: block; }
  .social .s1 { background: #6cc3e8; }
  .social .s2 { background: #e04a4a; }
  .social .s3 { background: #3b63b3; }
  .social .s4 { background: #3d3d3d; }

  .main-nav { position: absolute; left: 78px; top: 100px; width: 1000px; height: 34px; background: var(--nav-bg); display: flex; align-items: center; padding-left: 23px; }
  .main-nav a { color: var(--white); text-decoration: none; font-family: "Roboto Condensed", sans-serif; font-size: 15px; margin-right: 34px; }

  .hero { position: absolute; left: 78px; top: 134px; width: 1000px; height: 325px; background: linear-gradient(90deg, #6d5d55 0%, #a0908a 35%, #8f8a8c 65%, #b3a8a2 100%); }
  .hero-caption { position: absolute; left: 497px; top: 75px; width: 456px; height: 175px; background: rgba(40,38,37,0.72); display: flex; align-items: center; justify-content: center; text-align: center; font-family: "Roboto Condensed", sans-serif; font-size: 21px; line-height: 29px; color: var(--white); }
  .hero-caption em { font-style: normal; color: var(--highlight); }

  .founded-band { position: absolute; left: 78px; top: 459px; width: 1000px; height: 84px; background: var(--teal); }
  .founded-band svg { position: absolute; left: 42px; top: 26px; }
  .founded-band p { position: absolute; left: 102px; top: 23px; width: 810px; font-family: "Roboto Condensed", sans-serif; font-size: 18px; line-height: 24px; color: var(--white); }

  .section-title { position: absolute; font-family: "Roboto Condensed", sans-serif; font-weight: 500; font-size: 18px; color: var(--ink); }
  .about-title { left: 80px; top: 591px; }
  .results-title { left: 754px; top: 596px; }

  .about-photo { position: absolute; }
  .photo-team { left: 78px; top: 631px; width: 288px; height: 160px; background: linear-gradient(135deg, #dfe6ee, #b9c9dc 55%, #eef0f2); }
  .photo-site { left: 399px; top: 627px; width: 301px; height: 164px; background: linear-gradient(135deg, #5e7fb0, #c9d3df 55%, #d6a23a); }

  .about-copy { position: absolute; left: 79px; top: 809px; width: 627px; font-size: 12.4px; line-height: 16px; letter-spacing: 0.45px; text-align: justify; }
  .about-copy p { margin-bottom: 15px; }
  .about-copy .link-line { text-align: left; white-space: nowrap; letter-spacing: 0.2px; }

  .results-list { position: absolute; left: 756px; top: 632px; width: 312px; list-style: none; font-size: 12.4px; line-height: 16px; letter-spacing: 0.45px; }
  .results-list li { position: relative; padding-left: 22px; margin-bottom: 16px; }
  .results-list svg { position: absolute; left: 0; top: 2px; }

  .memberships { position: absolute; left: 88px; top: 1030px; width: 997px; height: 102px; border: 1px solid var(--panel-border); border-radius: 6px; background: linear-gradient(#f6f6f6, #ffffff); text-align: center; font-family: "Roboto Condensed", sans-serif; }
  .memberships h2 { font-weight: 500; font-size: 19px; color: var(--teal); margin-top: 14px; }
  .memberships p { font-size: 15px; color: #555; line-height: 20px; margin-top: 6px; }

  .footer-rule { position: absolute; left: 88px; top: 1157px; width: 1000px; height: 1px; background: #cccccc; }
  .footer-note { position: absolute; left: 0; width: 1256px; top: 1167px; text-align: center; font-size: 10px; letter-spacing: 1px; color: #8a8a8a; }
</style>
</head>
<body>
  <header>
    <div class="brand">Lindavo, Inc.</div>
    <div class="brand-divider"></div>
    <div class="tagline">community development and housing rehabilitation programs</div>
    <div class="social" aria-label="Social links"><span class="s1"></span><span class="s2"></span><span class="s3"></span><span class="s4"></span></div>
  </header>

  <nav class="main-nav">
    <a href="#">Home</a><a href="#">Our Company</a><a href="#">Housing Rehab Application</a><a href="#">Affordable Application</a><a href="#">Contact Us</a>
  </nav>

  <section class="hero" role="img" aria-label="Smiling man in a navy polo shirt in front of a softly blurred office with colleagues">
    <div class="hero-caption">
      <div>Over twenty years of experience in<br><em>developing</em> and <em>administering income</em><br><em>base-base housing</em> and <em>programs</em></div>
    </div>
  </section>

  <section class="founded-band">
    <svg width="34" height="34" viewBox="0 0 34 34" aria-hidden="true">
      <g fill="#ffffff" transform="translate(17 17)">
        <rect x="-3.5" y="-16" width="7" height="32" rx="1"/>
        <rect x="-3.5" y="-16" width="7" height="32" rx="1" transform="rotate(45)"/>
        <rect x="-3.5" y="-16" width="7" height="32" rx="1" transform="rotate(90)"/>
        <rect x="-3.5" y="-16" width="7" height="32" rx="1" transform="rotate(135)"/>
        <circle r="11.5"/>
      </g>
      <circle cx="17" cy="17" r="5" fill="#1e9198"/>
    </svg>
    <p>Founded in 1975, Lindavo has grown to be the only full service affordable housing implementation company in New Jersey.</p>
  </section>

  <h2 class="section-title about-title">About Lindavo</h2>
  <div class="about-photo photo-team" role="img" aria-label="Team in hard hats reviewing plans around a table"></div>
  <div class="about-photo photo-site" role="img" aria-label="Two construction workers in hard hats reading blueprints on site"></div>

  <div class="about-copy">
    <p>Lindavo, Inc. is a city planning firm that specializes in community development and housing rehabilitation program planning, design and implementation. We have over twenty years of experience in developing and administering income base-base housing and programs in accordance with National Office of Civic Housing Standards (NOCHS) and State Board on Fair Housing Placement (SBFHP) rules and regulations,</p>
    <p>In addition, our firm is capable of providing the technical and administrative assistance our clients require for implementation of their income based housing programs. M. Harlan Vesk Associates is one of the most experience urban planning firms in New Jersey, with over forty years of as consulting planners.</p>
    <p class="link-line">To find out more about federal housing programs that we will administer, please go to www.civichousinginfo.org</p>
  </div>

  <h2 class="section-title results-title">We Get Results:</h2>
  <ul class="results-list">
    <li><svg width="12" height="12" viewBox="0 0 12 12" aria-hidden="true"><polygon fill="#1e9198" points="6,0 7.6,4.1 12,4.4 8.6,7.2 9.7,11.5 6,9.1 2.3,11.5 3.4,7.2 0,4.4 4.4,4.1"/></svg>Lindavo designs income based programs to be supported by federal placement lotteries state funding.</li>
    <li><svg width="12" height="12" viewBox="0 0 12 12" aria-hidden="true"><polygon fill="#1e9198" points="6,0 7.6,4.1 12,4.4 8.6,7.2 9.7,11.5 6,9.1 2.3,11.5 3.4,7.2 0,4.4 4.4,4.1"/></svg>We implement local programs to benefit people seeking access to affordable housing. Our experienced staff screen applicants for local affordable housing.</li>
    <li><svg width="12" height="12" viewBox="0 0 12 12" aria-hidden="true"><polygon fill="#1e9198" points="6,0 7.6,4.1 12,4.4 8.6,7.2 9.7,11.5 6,9.1 2.3,11.5 3.4,7.2 0,4.4 4.4,4.1"/></svg>We pre-qualify persons who have applied for housing rehabilitation.<br>Conduct placement lotteries</li>
  </ul>

  <section class="memberships">
    <h2>Memberships</h2>
    <p>National Civic Renewal Association&nbsp;&nbsp;&nbsp;Garden State Planning Society<br>Regional Planning Officials Forum Statewide Neighborhood Growth Association</p>
  </section>

  <footer>
    <div class="footer-rule"></div>
    <div class="footer-note">Copy Right 2014 Lindavo, 218 Tessary Lane, Ardenwick, New Jersey, 08719&nbsp;&nbsp;&nbsp;TEL (555) 314-2260 Fax (555) 314-2281</div>
  </footer>
</body>
</html>
```